Alloy Wheels Wholesaler and Distributor Product Brochure Design

We need product Brochure design.
We are an alloy wheel distributor and need a sophisticated product catalogue/brochure to supply for our clients. Our website is www.tepvanco.com.au so you can have a look and get the idea.
Needs to be professional. I have a base concept of lay out, see attached.
The number of products per page is exactly how I need it, but arrangement and further enhancement to make it look better is what we looking for.
I would like all products to be on white background.

- Size will need to be DL format 98mm x 210mm with 2mm bleed
- Openable Horizontally ( landscape format )
- 12 pages ( see attached page by page guide )
- Final file needs to be print ready,

See files attached:
1. All product photos
2. List of products with names/description
3. Sample lay out of brochure how I see it pay by page
4. our existing logo, also have AI file if requested.
5. Text for second last page ( warranty and care instructions )
6. Some sample photos of vehicle that can be use on front page.

If I missed anything please message.

Target Market(s)

To be used by retail outlets to showcase the products as well as end clients to keep for their consideration when selecting a wheel for their vehicle.

Industry/Entity Type

Automotive

Colors
0455a3
3176b5
85acd3
ffffff

Requirements
Must have
• Professional look, in line with our general theme and exiting website.
Should not have
• we need it to be simple and minimum colours

```html
<!DOCTYPE html>
<html lang="en">
<head>
<meta charset="utf-8">
<title>Tepvanco – Contact Us</title>
<link rel="stylesheet" href="https://fonts.googleapis.com/css2?family=Tinos&display=swap">
<style>
  :root {
    --paper: #e9eaec;
    --brand-faint: #d9dadc;
    --rule: #7ba3d2;
    --ink: #111111;
    --car-dark: #1f2022;
    --car-mid: #4a4b4f;
    --wheel: #9a9ca0;
  }
  html, body {
    margin: 0;
    padding: 0;
    overflow: hidden;
    background: var(--paper);
  }
  .back-cover {
    position: relative;
    width: 1200px;
    height: 583px;
    overflow: hidden;
    background: var(--paper);
    font-family: "Tinos", "Times New Roman", serif;
    color: var(--ink);
  }
  .brand-name {
    position: absolute;
    left: 120px;
    top: 140px;
    margin: 0;
    font-size: 64px;
    font-weight: 400;
    line-height: 1;
    letter-spacing: 4px;
    color: var(--brand-faint);
  }
  .vehicle-photo {
    position: absolute;
    left: 0;
    top: 0;
    width: 1200px;
    height: 583px;
  }
  .rules {
    position: absolute;
    left: 0;
    top: 0;
    width: 1200px;
    height: 583px;
  }
  .rules line {
    stroke: var(--rule);
  }
  .contact-heading {
    position: absolute;
    left: 380px;
    top: 261px;
    margin: 0;
    font-size: 31px;
    font-weight: 400;
    line-height: 1;
  }
  .contact-list {
    list-style: none;
    margin: 0;
    padding: 0;
  }
  .contact-item {
    position: absolute;
    left: 234px;
    font-size: 31px;
    line-height: 1;
  }
  .contact-item.phone-free { top: 311px; }
  .contact-item.phone-local { top: 371px; }
  .contact-item.email { top: 426px; }
  .contact-item.web { top: 480px; }
</style>
</head>
<body>
<main class="back-cover">
  <p class="brand-name">TEPVANCO</p>

  <svg class="vehicle-photo" viewBox="0 0 1200 583" role="img" aria-label="Photo of a dark grey car's front wheel with a silver multi-spoke alloy rim">
    <defs>
      <radialGradient id="wheel-tone" cx="905" cy="340" r="300" gradientUnits="userSpaceOnUse">
        <stop offset="0" stop-color="var(--wheel)"/>
        <stop offset="0.55" stop-color="var(--car-mid)"/>
        <stop offset="1" stop-color="var(--car-dark)"/>
      </radialGradient>
    </defs>
    <path d="M710 0 L1200 0 L1200 583 L770 583 C705 545 655 470 648 400 C642 300 660 140 710 0 Z" fill="url(#wheel-tone)"/>
  </svg>

  <svg class="rules" viewBox="0 0 1200 583" aria-hidden="true">
    <line x1="0" y1="293" x2="570" y2="293" stroke-width="5"/>
    <line x1="233" y1="345" x2="645" y2="345" stroke-width="4"/>
    <line x1="233" y1="404" x2="660" y2="404" stroke-width="4"/>
    <line x1="233" y1="460" x2="712" y2="460" stroke-width="4"/>
    <line x1="233" y1="514" x2="748" y2="514" stroke-width="4"/>
  </svg>

  <h2 class="contact-heading">CONTACT US</h2>
  <ul class="contact-list">
    <li class="contact-item phone-free">1300 555 018</li>
    <li class="contact-item phone-local">(03) 5550 4821</li>
    <li class="contact-item email">sales@tepvanco.com.au</li>
    <li class="contact-item web">www.tepvanco.com.au</li>
  </ul>
</main>
</body>
</html>
```